Tervolan Pty Ltd professional business card

A professional business card template using the colours from the supplied logo.
Clean crisp lines while, Modern while not being over the top.

Target Market(s)

Construction, commerical and industrial

Industry/Entity Type

Communications

Contact Information for Business Card

For a Communications, IT, Optical fibre installation company

Colors
37b8a4

```html
<!DOCTYPE html>
<html lang="en">
<head>
<meta charset="utf-8">
<title>Tervolan Pty Ltd – Business Card</title>
<link rel="stylesheet" href="https://fonts.googleapis.com/css2?family=Fira+Sans:wght@400;600&family=Fira+Sans+Condensed:wght@300;400&display=swap">
<style>
  :root {
    --teal: #13909c;
    --teal-dark: #0f7b86;
    --paper: #ffffff;
    --ink-grey: #56585b;
    --backdrop: #c9d9d7;
  }
  * { margin: 0; padding: 0; box-sizing: border-box; }
  html, body { width: 1200px; height: 1200px; overflow: hidden; }
  body {
    background: var(--backdrop);
    display: flex;
    flex-direction: column;
    align-items: center;
    justify-content: center;
    gap: 60px;
    font-family: "Fira Sans Condensed", "Fira Sans", sans-serif;
  }
  .card {
    position: relative;
    width: 900px;
    height: 514px;
    background: var(--paper);
    overflow: hidden;
    box-shadow: 0 10px 28px rgba(40, 70, 70, 0.18);
  }
  .card svg.shape { position: absolute; inset: 0; }
  .wordmark {
    position: absolute;
    font-family: "Fira Sans", sans-serif;
    font-weight: 600;
    color: var(--ink-grey);
    letter-spacing: 2px;
    display: flex;
    align-items: center;
    gap: 14px;
    white-space: nowrap;
  }
  .wordmark .dot {
    display: inline-block;
    border-radius: 50%;
    background: var(--teal);
  }

  /* back side */
  .card-back .wordmark { left: 50%; top: 50%; transform: translate(-50%, -50%); font-size: 70px; }
  .card-back .wordmark .dot { width: 34px; height: 34px; }
  .corner-bar { position: absolute; background: var(--teal); height: 16px; width: 250px; }
  .corner-bar.top { top: 0; right: 0; }
  .corner-bar.bottom { bottom: 0; left: 0; }

  /* front side */
  .card-front .wordmark { right: 190px; top: 60px; font-size: 48px; }
  .card-front .wordmark .dot { width: 22px; height: 22px; }
  .holder { position: absolute; right: 60px; top: 228px; text-align: right; color: var(--paper); }
  .holder-name { font-family: "Fira Sans Condensed", sans-serif; font-weight: 300; font-size: 44px; line-height: 1; }
  .holder-title { font-weight: 300; font-size: 22px; margin-top: 6px; }
  .contact-list {
    position: absolute; left: 52px; top: 380px;
    list-style: none; color: var(--paper);
    font-weight: 300; font-size: 22px; line-height: 31px;
  }
  .contact-list li { display: flex; align-items: center; gap: 18px; }
  .contact-list svg { width: 16px; height: 16px; flex: none; }
  .address {
    position: absolute; right: 58px; top: 320px;
    color: var(--paper); font-weight: 300; font-size: 20px;
    display: flex; align-items: center; gap: 12px;
  }
  .address svg { width: 16px; height: 20px; }
</style>
</head>
<body>

<section class="card card-back" aria-label="Business card back">
  <span class="corner-bar top"></span>
  <span class="corner-bar bottom"></span>
  <div class="wordmark"><span class="dot"></span>TERVOLAN</div>
</section>

<section class="card card-front" aria-label="Business card front">
  <svg class="shape" viewBox="0 0 900 514" width="900" height="514" aria-hidden="true">
    <path d="M0 228 C 300 214 600 200 760 130 C 830 95 860 40 885 0 L900 0 L900 514 L0 514 Z" fill="var(--teal)"/>
    <line x1="390" y1="282" x2="660" y2="282" stroke="var(--paper)" stroke-width="2"/>
    <line x1="40" y1="362" x2="520" y2="362" stroke="var(--paper)" stroke-width="2"/>
  </svg>

  <div class="wordmark"><span class="dot"></span>TERVOLAN</div>

  <div class="holder">
    <p class="holder-name">Your Name Here</p>
    <p class="holder-title">Manager/CEO</p>
  </div>

  <p class="address">
    <svg viewBox="0 0 16 20" aria-hidden="true"><path d="M8 0a7 7 0 0 0-7 7c0 5 7 13 7 13s7-8 7-13a7 7 0 0 0-7-7zm0 10a3 3 0 1 1 0-6 3 3 0 0 1 0 6z" fill="var(--paper)"/></svg>
    your address goes here
  </p>

  <ul class="contact-list">
    <li><svg viewBox="0 0 16 16" aria-hidden="true"><path d="M3 1l3 3-2 2c1 2 3 4 5 5l2-2 3 3-2 3C7 15 1 9 1 3z" fill="var(--paper)"/></svg>123 - 456 - 7890</li>
    <li><svg viewBox="0 0 16 16" aria-hidden="true"><rect x="4" y="1" width="8" height="14" rx="1.5" fill="none" stroke="var(--paper)" stroke-width="1.6"/><circle cx="8" cy="12.5" r="1" fill="var(--paper)"/></svg>010 - 000 - 1234</li>
    <li><svg viewBox="0 0 16 16" aria-hidden="true"><rect x="1" y="3" width="14" height="10" fill="none" stroke="var(--paper)" stroke-width="1.6"/><path d="M1 3l7 6 7-6" fill="none" stroke="var(--paper)" stroke-width="1.6"/></svg>info@youremail.com</li>
    <li><svg viewBox="0 0 16 16" aria-hidden="true"><circle cx="8" cy="8" r="6.5" fill="none" stroke="var(--paper)" stroke-width="1.4"/><path d="M1.5 8h13M8 1.5c-3 3.5-3 9.5 0 13M8 1.5c3 3.5 3 9.5 0 13" fill="none" stroke="var(--paper)" stroke-width="1.2"/></svg>www.yourwebsite.com</li>
  </ul>
</section>

</body>
</html>
```